Office Warming Party. I attached an image (blogger flyer) that you can use as an example, or you can create one from scratch. I just want it to look clean but stylish like the example (but still professional). Text:

(ps if there is too much text, you can take out the last line and just put brantleylawgroup.com)

BRANTLEY LAW GROUP (logo attached with the skyline image, I will provide a better quality logo but this will work for the proof)

OFFICE WARMING PARTY
FRI NOV 15 2013 7-10PM
2847 K Avenue, Suite 415
Sacramento

Full Hosted Bar / Cocktail Attire

Music by SF's Marcus Tilden (larger text)
Also feat. Leon Whitfield & Vanto
Catering by Pimento, Tidewell, and Harubo

Also a birthday party for Oswin Brantley. Invite only. Please RSVP
at www.eventplaza.example/events/604839127748213

BRANTLEY LAW GROUP specializes in personal injury and criminal law, visit our site
at www.brantleylawgroup.com or call (916) 555-0173 for more information

It's not letting me attach the flyers so I'm including links to them:
http://www.gigposterhub.example/images/uploads/flyers/blogger_holiday_party.jpg

http://www.capitolclaims.example (brantley law group is top left)

Target Market(s)

Professionals but also house music lovers

Industry/Entity Type

Catering

Font styles to use
Sans Serif

Requirements
Must have
• Logo and DJ name bold or bigger (Marcus Tilden)

```html
<!DOCTYPE html>
<html lang="en">
<head>
<meta charset="utf-8">
<title>Brantley Law Group – Office Warming Party</title>
<link rel="stylesheet" href="https://fonts.googleapis.com/css2?family=Federo&display=swap">
<style>
  :root {
    --red: #c8101c;
    --ink: #2b2b2b;
    --grey: #6a6a6a;
    --grey-light: #9a9a9a;
    --rule: #c9c9c9;
    --bg-top: #f7f7f7;
    --bg-bottom: #e6e6e6;
  }
  * { margin: 0; padding: 0; box-sizing: border-box; }
  html, body { width: 848px; height: 1200px; overflow: hidden; }
  body { font-family: "Federo", sans-serif; color: var(--ink); }
  .flyer {
    position: relative;
    width: 848px;
    height: 1200px;
    background: radial-gradient(ellipse at 40% 40%, var(--bg-top) 0%, #efefef 55%, var(--bg-bottom) 100%);
    overflow: hidden;
  }
  .backdrop {
    position: absolute; inset: 0;
    background: linear-gradient(135deg, rgba(0,0,0,0) 30%, rgba(0,0,0,0.03) 50%, rgba(0,0,0,0) 70%);
  }
  .line { position: absolute; left: 0; width: 100%; line-height: 1; white-space: nowrap; }
  .rule { position: absolute; left: 100px; width: 648px; height: 1px; background: var(--rule); }
  .brand { top: 110px; left: 100px; font-size: 36px; color: var(--grey); letter-spacing: 1px; }
  .title { color: var(--red); }
  .title-office { top: 188px; left: 164px; font-size: 106px; }
  .title-party { top: 270px; left: 122px; font-size: 84px; }
  .date { top: 402px; left: 146px; font-size: 52px; color: var(--grey); }
  .address { top: 458px; left: 146px; font-size: 28px; color: var(--grey-light); display: flex; align-items: center; gap: 8px; }
  .dress { top: 546px; font-size: 34px; display: flex; justify-content: center; align-items: center; gap: 8px; }
  .music-by { top: 634px; font-size: 34px; display: flex; justify-content: center; align-items: center; gap: 10px; padding-right: 40px; }
  .headliner { top: 690px; text-align: center; font-size: 52px; color: var(--red); }
  .featuring { top: 748px; text-align: center; font-size: 32px; color: var(--ink); }
  .featuring .soft { color: var(--grey-light); }
  .catering { top: 832px; font-size: 28px; display: flex; justify-content: center; align-items: center; gap: 10px; color: var(--grey); }
  .catering b, .featuring b { font-weight: normal; color: var(--ink); }
  .invite { top: 898px; left: 126px; font-size: 26px; color: var(--grey); display: flex; align-items: center; gap: 10px; }
  .celebrants { top: 936px; left: 170px; font-size: 26px; color: var(--ink); }
  .celebrants .name { color: var(--red); }
  .rsvp { top: 986px; text-align: center; font-size: 28px; color: var(--grey); }
  .rsvp b { font-weight: normal; color: var(--ink); }
  .about { top: 1046px; text-align: center; font-size: 19px; color: var(--ink); }
  .contact { top: 1076px; text-align: center; font-size: 18px; color: var(--red); }
  .contact b { font-weight: normal; color: var(--ink); }
</style>
</head>
<body>
<main class="flyer">
  <div class="backdrop" role="img" aria-label="Large faint linked-chain decoration across the background"></div>

  <div class="line brand">BRANTLEY LAW GROUP</div>
  <div class="rule" style="top:164px"></div>

  <h1 class="title">
    <span class="line title-office">OFFICE</span>
    <span class="line title-party">WARMING PARTY</span>
  </h1>
  <div class="rule" style="top:388px"></div>

  <div class="line date">FRI NOV 15 2013 7-10PM</div>
  <div class="line address">
    <svg width="18" height="26" viewBox="0 0 18 26" aria-hidden="true"><path d="M9 0C4 0 0 4 0 9c0 7 9 17 9 17s9-10 9-17C18 4 14 0 9 0z" fill="var(--red)"/><circle cx="9" cy="9" r="3.5" fill="#f2f2f2"/></svg>
    2847 K Avenue, Suite 415, Sacramento
  </div>
  <div class="rule" style="top:512px"></div>

  <div class="line dress">
    Full Hosted Bar
    <svg width="26" height="38" viewBox="0 0 26 38" aria-hidden="true"><path d="M2 2h22c0 9-4 15-11 15S2 11 2 2z" fill="var(--red)"/><rect x="12" y="17" width="2" height="15" fill="var(--red)"/><rect x="5" y="32" width="16" height="3" rx="1" fill="var(--red)"/></svg>
    Cocktail Attire
  </div>
  <div class="rule" style="top:610px"></div>

  <div class="line music-by">
    <svg width="48" height="30" viewBox="0 0 48 30" aria-hidden="true"><path d="M2 14 L24 4 L46 14 L24 26 Z" fill="var(--red)"/><ellipse cx="22" cy="15" rx="9" ry="5" fill="#fff"/><ellipse cx="22" cy="15" rx="2.5" ry="1.4" fill="var(--red)"/><path d="M2 14 v4 L24 30 v-4 Z M46 14 v4 L24 30 v-4 Z" fill="#8e0b14"/></svg>
    Music by
  </div>
  <div class="line headliner">SF's Marcus Tilden</div>
  <div class="line featuring"><span class="soft">also feat.</span> <b>Leon Whitfield &amp; Vanto</b></div>
  <div class="rule" style="top:810px"></div>

  <div class="line catering">
    <svg width="28" height="34" viewBox="0 0 28 34" aria-hidden="true"><rect x="1" y="0" width="2" height="10" fill="var(--red)"/><rect x="5" y="0" width="2" height="10" fill="var(--red)"/><rect x="1" y="9" width="6" height="3" fill="var(--red)"/><rect x="3" y="10" width="2.5" height="24" fill="var(--red)"/><rect x="11" y="0" width="4" height="34" rx="2" fill="var(--red)"/><ellipse cx="23" cy="7" rx="4" ry="7" fill="var(--red)"/><rect x="21.8" y="12" width="2.5" height="22" fill="var(--red)"/></svg>
    Catering by <b>Pimento, Tidewell, and Harubo</b>
  </div>
  <div class="rule" style="top:882px"></div>

  <div class="line invite">
    Invite only.
    <svg width="30" height="26" viewBox="0 0 30 26" aria-hidden="true"><rect x="3" y="10" width="24" height="15" fill="var(--red)"/><rect x="3" y="15" width="24" height="2" fill="#fff"/><rect x="8" y="3" width="2" height="7" fill="var(--red)"/><rect x="14" y="3" width="2" height="7" fill="var(--red)"/><rect x="20" y="3" width="2" height="7" fill="var(--red)"/></svg>
    Also a Birthday Celebration for
  </div>
  <div class="line celebrants"><span class="name">Oswin Brantley</span> (11/15) and <span class="name">Renata Vale</span> (11/16)</div>
  <div class="rule" style="top:972px"></div>

  <div class="line rsvp">RSVP at <b>www.eventplaza.example/events/604839127748213</b></div>
  <div class="rule" style="top:1024px"></div>

  <div class="line about">BRANTLEY LAW GROUP specializes in personal injury and criminal law.</div>
  <div class="line contact">Visit <b>www.brantleylawgroup.com</b> or call <b>(916) 555-0173</b> for more information.</div>
</main>
</body>
</html>
```